Business Card Design for a Technology Development Company

******* PLEASE NOTE (ALL DESIGNERS): I am going to finish the competition on Monday the 9th July (NOT SATURDAY 15TH). I have some designs I like and need to get them printed next week. Please submit any designs today or tomorrow. *******

PLEASE READ ALL OF THE REQUIREMENTS!!! I've rejected lot's of designs in the past because they didn't read the basic requirements - thanks and good luck!

Quill Harbor is a UK technology / small holding company that invests in startups and develops new ideas. In addition it provides IT Professional Services.

Ideally the design will be simple, professional, smart, and sophisticated, and overall be nice to look at. You can be creative as you like with the design, equally as simple as you like - you guys are the professionals so I'll leave it to your inspiration (make sure you incorporate the logo)!
Updates

PLEASE NOTE (ALL DESIGNERS): I am going to finish the competition on Monday the 9th July (NOT SATURDAY 15TH).  I have some designs I like and need to get them printed next week.  Please submit any designs today or tomorrow.

Target Market(s)

Enterprises / corporations / public sector / technical engineers / investors. More www.brantelix.com / www.vornel.com than www.pibbleroo.com!

Industry/Entity Type

Business

Requirements
Must have
• It should be modern and any artwork (if used) should be simple
- Pastel colours, dark and light colours, and shades are preferred over bright colours
- The design should incorporate the attached Quill Harbor logo and the logo colour scheme
- The logo should be on both sides. The back should just have the logo, maybe with some additional graphics
- It must have the following information on:

FirstName SecondName
Company Position
Email: name@quillharbor.co.uk
Mobile: +44 (0) 7700 984312

- The final design should be for a UK business card, dimensions: 85mm × 55mm
- The final design should have bleed marks to allow for printing and should be given in vector formats (EPS and AI)
Nice to have
• The Logo can be separated from the font in the logo on the front of the card. This isn't necessary or required, just to know it's not a limitation.
Should not have
• No bright colours (I prefer pastel colours, dark and light colours, and shades)
- Fonts that are to thin
- Effects or designs that make it difficult to print
- Italic or old fashioned looking fonts, i.e. anything like Times New Roman is a NO!

```html
<!DOCTYPE html>
<html lang="en">
<head>
<meta charset="utf-8">
<title>Quill Harbor – Business Card</title>
<link rel="stylesheet" href="https://fonts.googleapis.com/css2?family=Questrial&family=Source+Sans+3:wght@400;600;700&display=swap">
<style>
  :root {
    --teal: #0f8ba3;
    --teal-light: #7fd0e2;
    --ink: #3a3a3a;
    --card: #ffffff;
    --backdrop: #e8e5e1;
  }
  * { box-sizing: border-box; margin: 0; padding: 0; }
  html, body {
    width: 1200px;
    height: 412px;
    overflow: hidden;
    background: var(--backdrop);
  }
  .sheet {
    position: relative;
    width: 1200px;
    height: 412px;
  }
  .card {
    position: absolute;
    top: 64px;
    width: 498px;
    height: 285px;
    background: var(--card);
    border-radius: 38px;
    overflow: hidden;
    border: 1px solid #d6d2cc;
  }
  .card--front { left: 71px; }
  .card--back { left: 633px; }

  .brand {
    position: absolute;
    top: 34px;
    left: 0;
    right: 0;
    display: flex;
    align-items: center;
    justify-content: center;
    gap: 18px;
    height: 80px;
  }
  .brand__dot {
    width: 48px;
    height: 48px;
    border-radius: 50%;
    background: var(--teal);
    flex: none;
  }
  .brand__name {
    font-family: "Questrial", sans-serif;
    font-size: 40px;
    color: var(--teal);
    letter-spacing: 0.5px;
    white-space: nowrap;
  }

  .name-band {
    position: absolute;
    left: 0;
    right: 0;
    top: 143px;
    height: 45px;
    border-top: 2px solid var(--teal);
    border-bottom: 2px solid var(--teal);
    padding: 2px 0;
    background: var(--card);
  }
  .name-band__fill {
    height: 100%;
    background: var(--teal-light);
    display: flex;
    align-items: center;
    justify-content: center;
    font-family: "Source Sans 3", sans-serif;
    color: var(--teal);
  }
  .name-band__name { font-weight: 700; font-size: 17px; }
  .name-band__title { font-weight: 400; font-size: 14px; margin-left: 5px; }

  .contact {
    position: absolute;
    left: 0;
    right: 0;
    font-family: "Source Sans 3", sans-serif;
    color: var(--ink);
    font-size: 13px;
    text-align: center;
  }
  .contact--lines { top: 205px; }
  .contact__row {
    display: flex;
    align-items: center;
    justify-content: center;
    gap: 7px;
    height: 18px;
  }
  .contact__row + .contact__row { margin-top: 6px; }
  .contact__item { display: inline-flex; align-items: center; gap: 2px; }
  .contact__item svg { width: 12px; height: 12px; fill: var(--teal); flex: none; }

  .website {
    position: absolute;
    left: 0;
    right: 0;
    top: 262px;
    text-align: center;
    font-family: "Source Sans 3", sans-serif;
    font-weight: 700;
    font-size: 13.5px;
    letter-spacing: 3px;
    color: var(--teal);
    line-height: 1;
  }
  .card--back .website { top: 264px; }
</style>
</head>
<body>
<main class="sheet">
  <section class="card card--front" aria-label="Business card front">
    <div class="brand">
      <span class="brand__dot"></span>
      <span class="brand__name">Quill Harbor</span>
    </div>

    <div class="name-band">
      <div class="name-band__fill">
        <span class="name-band__name">Your Name,</span>
        <span class="name-band__title">Title</span>
      </div>
    </div>

    <div class="contact contact--lines">
      <div class="contact__row">
        <span class="contact__item">
          <svg viewBox="0 0 24 24" aria-hidden="true"><path d="M6.6 10.8a15.1 15.1 0 0 0 6.6 6.6l2.2-2.2c.3-.3.7-.4 1-.2 1.1.4 2.3.6 3.6.6.6 0 1 .4 1 1V20c0 .6-.4 1-1 1A17 17 0 0 1 3 4c0-.6.4-1 1-1h3.5c.6 0 1 .4 1 1 0 1.3.2 2.5.6 3.6.1.3 0 .7-.2 1z"/></svg>
          +123 456 7890
        </span>
        <span class="contact__item">
          <svg viewBox="0 0 24 24" aria-hidden="true"><path d="M7 1h10a2 2 0 0 1 2 2v18a2 2 0 0 1-2 2H7a2 2 0 0 1-2-2V3a2 2 0 0 1 2-2zm0 3v13h10V4zm5 15a1.2 1.2 0 1 0 0 2.4 1.2 1.2 0 0 0 0-2.4z"/></svg>
          +44 (0) 7700 984312
        </span>
        <span class="contact__item">
          <svg viewBox="0 0 24 24" aria-hidden="true"><path d="M2 5h20v14H2zm2 2v.5l8 5 8-5V7zm0 2.9V17h16V9.9l-8 5z"/></svg>
          name@quillharbor.co.uk
        </span>
      </div>
      <div class="contact__row">Complex Name, Street Name, Area, City Name,000 000</div>
    </div>

    <p class="website">www.quillharbor.com</p>
  </section>

  <section class="card card--back" aria-label="Business card back">
    <div class="brand">
      <span class="brand__dot"></span>
      <span class="brand__name">Quill Harbor</span>
    </div>
    <p class="website">www.quillharbor.com</p>
  </section>
</main>
</body>
</html>
```